Quick Banner Ad Job for IT Services Company

Need a collection of banner ads based around a common theme and message.

Main Theme.

IT Support and Managed Services - IT support you can rely on.
Free remote monitoring and alerting*
*conditions apply <-- this in small text

Secondary Content

Our customers are attracted by our exceptional level of customer service and trust us in providing them with support and advice over a long term relationship.

Note:
* Logos and colours attached. Only use these colours.
* Font is to be Myriad Pro

* Delivery will require the following sizes.
Leaderboard: 728×90
Medium Rectangle: 300×250
Wide Skyscraper: 160×600

Do the initial draft in leaderboard, other sizes can be worked once we have an agreed design for the main

Final delivery will also need to be in an editable format, not just final images.

Industry/Entity Type

It Company

```html
<!DOCTYPE html>
<html lang="en">
<head>
<meta charset="utf-8">
<title>NovaLink IT Support Leaderboard Banners</title>
<link rel="stylesheet" href="https://fonts.googleapis.com/css2?family=Source+Sans+3:ital,wght@0,400;0,700;1,400&display=swap">
<style>
  :root {
    --page-bg: #e9e1d3;
    --sky: #1fb3e8;
    --sky-deep: #1890c4;
    --ocean: #1b5f86;
    --navy: #0f3f5e;
    --ink: #111820;
    --brand-ink: #173c5c;
    --white: #ffffff;
  }
  * { box-sizing: border-box; margin: 0; padding: 0; }
  html, body {
    width: 1200px; height: 1200px; overflow: hidden;
    background: var(--page-bg);
    font-family: "Source Sans 3", "Myriad Pro", sans-serif;
  }
  .leaderboard {
    position: absolute; left: 115px; width: 970px; height: 120px;
    overflow: hidden;
  }
  .leaderboard--light { top: 427px; }
  .leaderboard--dark { top: 582px; }
  .leaderboard__shapes { position: absolute; inset: 0; width: 100%; height: 100%; }

  .brand {
    position: absolute; left: 0; top: 0; width: 122px; height: 120px;
    display: flex; align-items: center; justify-content: center; gap: 5px;
  }
  .brand__dot { width: 12px; height: 12px; border-radius: 50%; background: var(--sky); }
  .brand__name { font-weight: 700; font-size: 21px; color: var(--brand-ink); letter-spacing: -0.3px; }

  .message {
    position: absolute; left: 170px; width: 400px; top: 0; height: 120px;
    text-align: center;
  }
  .message__headline {
    position: absolute; left: 0; right: 0;
    font-weight: 700; font-size: 24.5px; line-height: 1; white-space: nowrap;
  }
  .message__headline--first { top: 13px; }
  .message__headline--second { top: 45px; }
  .message__offer {
    position: absolute; left: 0; right: 0; top: 78px;
    font-style: italic; font-size: 24px; line-height: 1; color: var(--white); white-space: nowrap;
  }
  .message__terms {
    position: absolute; right: -5px; top: 105px;
    font-size: 10px; line-height: 1;
  }
  .leaderboard--light .message__headline { color: var(--ink); }
  .leaderboard--light .message__terms { color: var(--navy); }
  .leaderboard--dark .message__headline { color: var(--white); }
  .leaderboard--dark .message__terms { color: var(--white); }

  .promise {
    position: absolute; right: 60px; top: 13px; width: 260px;
    text-align: right; font-size: 13.2px; line-height: 17px; color: var(--ink);
  }
  .leaderboard--dark .promise { font-style: italic; color: var(--navy); }
</style>
</head>
<body>

<section class="leaderboard leaderboard--light" aria-label="Leaderboard banner, light version">
  <svg class="leaderboard__shapes" viewBox="0 0 970 120" preserveAspectRatio="none" aria-hidden="true">
    <defs>
      <linearGradient id="lightBody" x1="0" y1="0" x2="1" y2="1">
        <stop offset="0" stop-color="#22b6ea"/>
        <stop offset="0.45" stop-color="#1a9fd6"/>
        <stop offset="0.8" stop-color="#1b6e98"/>
        <stop offset="1" stop-color="#185a80"/>
      </linearGradient>
      <linearGradient id="lightWave" x1="0" y1="0" x2="1" y2="0">
        <stop offset="0" stop-color="#1b5f86"/>
        <stop offset="1" stop-color="#2aa6db"/>
      </linearGradient>
    </defs>
    <rect class="body" width="970" height="120" fill="url(#lightBody)"/>
    <path class="wave" d="M590 120 C660 100 680 40 690 0 H970 V120 Z" fill="url(#lightWave)"/>
    <path class="panel" d="M609 109 C670 80 690 40 700 9 H945 C958 9 962 18 958 35 L945 90 C941 104 932 109 918 109 Z" fill="var(--white)"/>
    <path class="logo-field" d="M0 0 H125 C138 40 128 90 90 120 H0 Z" fill="var(--white)"/>
  </svg>
  <div class="brand"><span class="brand__dot"></span><span class="brand__name">NovaLink</span></div>
  <div class="message">
    <p class="message__headline message__headline--first">IT Support and Managed Services</p>
    <p class="message__headline message__headline--second">- &nbsp;IT support you can rely on</p>
    <p class="message__offer">Free remote monitoring and alerting*</p>
    <p class="message__terms">*conditions apply</p>
  </div>
  <p class="promise">Our customers are attracted by<br>our exceptional level of customer<br>service and trust us in providing<br>them with support and advice over a<br>ong term relationship.</p>
</section>

<section class="leaderboard leaderboard--dark" aria-label="Leaderboard banner, dark version">
  <svg class="leaderboard__shapes" viewBox="0 0 970 120" preserveAspectRatio="none" aria-hidden="true">
    <defs>
      <linearGradient id="darkBody" x1="0" y1="0" x2="1" y2="1">
        <stop offset="0" stop-color="#0f4466"/>
        <stop offset="0.5" stop-color="#1b6690"/>
        <stop offset="0.75" stop-color="#1a84b8"/>
        <stop offset="1" stop-color="#0f3f5e"/>
      </linearGradient>
      <linearGradient id="darkWave" x1="0" y1="0" x2="1" y2="0">
        <stop offset="0" stop-color="#1b5f86"/>
        <stop offset="1" stop-color="#0f3552"/>
      </linearGradient>
    </defs>
    <rect class="body" width="970" height="120" fill="url(#darkBody)"/>
    <path class="wave" d="M590 120 C660 100 680 40 690 0 H970 V120 Z" fill="url(#darkWave)"/>
    <path class="panel" d="M609 109 C670 80 690 40 700 9 H945 C958 9 962 18 958 35 L945 90 C941 104 932 109 918 109 Z" fill="var(--sky)"/>
    <path class="logo-field" d="M0 0 H125 C138 40 128 90 90 120 H0 Z" fill="var(--white)"/>
  </svg>
  <div class="brand"><span class="brand__dot"></span><span class="brand__name">NovaLink</span></div>
  <div class="message">
    <p class="message__headline message__headline--first">IT Support and Managed Services</p>
    <p class="message__headline message__headline--second">- &nbsp;IT support you can rely on</p>
    <p class="message__offer">Free remote monitoring and alerting*</p>
    <p class="message__terms">*conditions apply</p>
  </div>
  <p class="promise">Our customers are attracted by<br>our exceptional level of customer<br>service and trust us in providing<br>them with support and advice over a<br>ong term relationship.</p>
</section>

</body>
</html>
```